Upmarket Bathroom and Kitchen ware supplier needs a classy business card design

We are a company based in Fiji, we sell plumbing ware (Kitchen and bathroom taps, Basins,showers, toilets etc) through up market show rooms to individuals and directly through Architects and designers of resorts and holiday houses for new builds and renovations. we are wanting to upgrade our over all look and brand. we are starting with a new logo but will be rebranding the whole business. This project is for a business card design for my management and tales team I would like it to be dark, classy and interesting

Target Market(s)

Resort directors and Management, High end holiday home owners

Contact Information for Business Card

Neil Dawson
Director
+64219473815

Colors

Designer to choose colors to be used in the design.

Requirements
Must have
• Must have an upmarket appearance I like darker charcoal shades but will be guided by the designers
• Please any catch phrases like "Crafting remarkable living rooms" this belongs tpo one of our suppliers so can not be used.
Nice to have
• Double sided, so front dedicated to logo provided and back info about the business and the person.

```html
<!DOCTYPE html>
<html lang="en">
<head>
<meta charset="utf-8">
<title>Haven Interiors – Business Card</title>
<link href="https://fonts.googleapis.com/css2?family=Montserrat:wght@300;400;500&display=swap" rel="stylesheet">
<style>
  :root {
    --backdrop: #2a2a2b;
    --card: #1c1d1f;
    --card-pattern-a: #202124;
    --card-pattern-b: #17181a;
    --ink: #f2f2f2;
    --ink-soft: #bdbdbd;
    --rule: #8a8a8a;
  }
  html, body {
    margin: 0;
    padding: 0;
    width: 1200px;
    height: 1108px;
    overflow: hidden;
    background: var(--backdrop);
    font-family: "Montserrat", sans-serif;
  }
  .stage {
    position: relative;
    width: 1200px;
    height: 1108px;
  }
  .card {
    position: absolute;
    top: 224px;
    width: 420px;
    height: 660px;
    border-radius: 26px;
    background: var(--card);
    overflow: hidden;
    box-shadow: 0 18px 40px rgba(0,0,0,.35);
  }
  .card--front { left: 150px; }
  .card--back { left: 630px; }

  .brand {
    position: absolute;
    top: 190px;
    left: 0;
    right: 0;
    text-align: center;
    color: var(--ink);
    font-weight: 300;
    font-size: 26px;
    letter-spacing: 0.32em;
    text-indent: 0.32em;
  }

  .person {
    position: absolute;
    top: 420px;
    left: 0;
    right: 0;
    text-align: center;
    color: var(--ink);
  }
  .person__name {
    font-weight: 500;
    font-size: 22px;
    letter-spacing: 0.08em;
    margin: 0;
  }
  .person__role {
    font-weight: 300;
    font-size: 13px;
    letter-spacing: 0.06em;
    color: var(--ink-soft);
    margin: 2px 0 0;
  }
  .divider {
    position: relative;
    width: 190px;
    height: 22px;
    margin: 10px auto 6px;
  }
  .divider::before {
    content: "";
    position: absolute;
    left: 0;
    right: 0;
    top: 50%;
    border-top: 1px solid var(--rule);
  }
  .divider svg {
    position: absolute;
    left: 50%;
    top: 0;
    transform: translateX(-50%);
  }
  .person__phone {
    font-weight: 400;
    font-size: 23px;
    letter-spacing: 0.04em;
    margin: 0;
  }

  .back-pattern {
    position: absolute;
    inset: 0;
    background: linear-gradient(135deg, var(--card-pattern-a), var(--card-pattern-b));
  }
  .back-brand {
    position: absolute;
    right: 40px;
    bottom: 96px;
    color: var(--ink);
    font-weight: 300;
    font-size: 12px;
    letter-spacing: 0.24em;
  }
</style>
</head>
<body>
<main class="stage">
  <section class="card card--front" aria-label="Business card front">
    <div class="brand">HAVEN INTERIORS</div>
    <div class="person">
      <p class="person__name">NEIL DAWSON</p>
      <p class="person__role">Director</p>
      <div class="divider">
        <svg width="22" height="22" viewBox="0 0 22 22" aria-hidden="true">
          <circle cx="11" cy="11" r="10" fill="var(--ink)"/>
          <path d="M7.2 6.5c.6-.5 1.3-.4 1.7.2l.9 1.4c.3.5.2 1.1-.2 1.4l-.6.5c.5 1.1 1.3 2 2.4 2.6l.5-.6c.4-.4 1-.5 1.4-.2l1.4.9c.6.4.7 1.1.2 1.7l-.6.7c-.6.6-1.6.7-2.6.2-2.2-1.1-3.9-2.8-5-5-.5-1-.4-2 .2-2.6z" fill="var(--card)"/>
        </svg>
      </div>
      <p class="person__phone">+64219473815</p>
    </div>
  </section>

  <section class="card card--back" aria-label="Business card back">
    <div class="back-pattern" role="img" aria-label="Faint repeating brand pattern across the card back"></div>
    <div class="back-brand">HAVEN INTERIORS</div>
  </section>
</main>
</body>
</html>
```